Stationery Design Project

Would like to have the design elements we created in for our website (www.brook-estates.com), incorporated in a stationery design layout.
Updates
Colors used in the logo attachments do not need to be used. We are open to different color variations. Looking for a crisp, clean, modern update using the design elements in attachments and which can also be viewed on or website.
A note to designers:
Project Deadline Extended
Reason: Due to update in our project description and requirements, we have decided to extend the deadline of this project to provide ample opportunity to all designers participating .
Requirements
Must have
- Must have continuity with the theme and design features used in our website. Have attached .jpg images of some of the design elements.

```html
<!DOCTYPE html>
<html lang="en">
<head>
<meta charset="utf-8">
<title>Brook Estates, Inc. — Letterhead</title>
<link rel="stylesheet" href="https://fonts.googleapis.com/css2?family=Tinos&display=swap">
<style>
  :root {
    --paper: #ffffff;
    --brand-green: #4fae3a;
    --forest: #033d22;
    --lime: #8cc63f;
    --lime-soft: #9dd056;
    --ink: #0b3a22;
    --edge: #d6d6d6;
  }
  html, body {
    margin: 0;
    padding: 0;
    overflow: hidden;
    background: var(--paper);
  }
  .letterhead {
    position: relative;
    width: 926px;
    height: 1200px;
    overflow: hidden;
    background: var(--paper);
    box-shadow: inset 0 0 0 1px var(--edge);
    font-family: "Tinos", "Times New Roman", serif;
  }
  .company-name {
    position: absolute;
    left: 58px;
    top: 44px;
    margin: 0;
    font-size: 60px;
    font-weight: 400;
    line-height: 1;
    letter-spacing: 0.5px;
    color: var(--brand-green);
  }
  .contact {
    position: absolute;
    left: 628px;
    top: 48px;
    margin: 0;
    font-style: normal;
    font-size: 17px;
    line-height: 25.5px;
    color: var(--ink);
  }
  .contact span { display: block; }
  .footer-swoosh {
    position: absolute;
    left: 0;
    top: 0;
    width: 926px;
    height: 1200px;
  }
</style>
</head>
<body>
  <main class="letterhead">
    <h1 class="company-name">Brook Estates, Inc.</h1>

    <address class="contact">
      <span>418 Alder Mill Road Suite 305</span>
      <span>Riverton, GA 30999</span>
      <span>PHONE: (555) 214-6630</span>
      <span>FAX: (555) 214-6631</span>
      <span>E-mail: info@brook-estates.com</span>
    </address>

    <svg class="footer-swoosh" viewBox="0 0 926 1200" aria-hidden="true">
      <defs>
        <linearGradient id="leaf-area-tone" x1="0" y1="0" x2="1" y2="1">
          <stop offset="0" stop-color="var(--lime-soft)"/>
          <stop offset="1" stop-color="var(--lime)"/>
        </linearGradient>
      </defs>
      <path class="band-dark" fill="var(--forest)"
            d="M0,1200 C330,1176 760,1090 926,871 L926,1200 Z"/>
      <path class="band-light" fill="var(--lime)"
            d="M40,1200 C420,1182 800,1118 926,906 L926,1200 Z"/>
      <rect class="leaf-motif" x="668" y="1072" width="234" height="100" rx="46"
            fill="url(#leaf-area-tone)" role="img" aria-label="Faint outline illustration of a leaf"/>
    </svg>
  </main>
</body>
</html>
```